Webdesign für Beratung und Service im Bereich Heizungs- und Kühltechnologie
Zielgruppe
Wir sind ein modernes Dienstleistungsunternehmen, dass im Bereich Beratung und Service für Heizungs- und Kühltechnologie tätig ist. Wir suchen ein modernes Webdesign, das sich überwiegend an Geschäfts- / Gewerbekunden richten soll.
Aufgabenstellung
Wir möchten die in unserem Logo verwendete Farben auf der Webseite wiederfinden, Bilder werden mitgeliefert, müssen aber keine Verwendung finden. Wichtig ist das Hervorheben als Kundendienstvertretung des Premium-Herstellers BRK mit deren Logo und direktem Link auf deren Webseite. Gerne würden wir einen modernen Ansatz sehen, abweichend von den Standard-Seiten anderer Wartungsfirmen in unserer Branche.

```html
<!DOCTYPE html>
<html lang="de">
<head>
<meta charset="utf-8">
<title>Vantherm GmbH – Heizungs- und Kühltechnologie</title>
<link href="https://fonts.googleapis.com/css2?family=Fira+Sans:wght@300;400;500;600;700&display=swap" rel="stylesheet">
<style>
:root{
  --navy:#0d3a66;
  --navy-dark:#0a2f55;
  --red:#c0393b;
  --red-dark:#9b2528;
  --red-text:#a3282b;
  --text:#2b2b2b;
  --muted:#9a9a9a;
  --gray-bg:#f5f5f5;
  --white:#ffffff;
  --line:#d9d9d9;
}
*{box-sizing:border-box;margin:0;padding:0}
html,body{width:1200px;height:2638px;overflow:hidden;background:var(--white)}
body{font-family:"Fira Sans",Arial,sans-serif;color:var(--text);position:relative}
.abs{position:absolute}
.backdrop{position:absolute;left:0;top:0}
/* header */
.brand{left:222px;top:10px;color:var(--navy)}
.brand-name{font-size:26px;font-weight:700;display:flex;align-items:center;gap:8px;line-height:1}
.brand-dot{width:14px;height:14px;border-radius:50%;background:var(--navy);display:inline-block}
.brand-tag{font-size:7px;font-weight:600;margin-top:10px;letter-spacing:.1px}
.main-nav{right:220px;top:24px;display:flex;gap:12px;font-size:10px;color:var(--white);text-transform:uppercase;letter-spacing:.2px}
.main-nav span.sep{opacity:.8}
/* hero */
.hero-text{left:222px;top:154px;width:330px}
.hero-kicker{color:var(--red-text);font-size:12px;font-weight:300}
.hero-title{color:var(--navy);font-size:22px;font-weight:700;line-height:26px;margin-top:4px}
.hero-lead{font-size:11.5px;line-height:16px;margin-top:40px;font-weight:400}
/* contact cards */
.card{background:var(--white);box-shadow:0 2px 14px rgba(0,0,0,.07)}
.contact-wide{left:222px;top:489px;width:758px;height:73px;display:flex}
.contact-wide .cell{flex:1;text-align:center;padding-top:16px;font-size:9.5px}
.contact-cell-icon{display:block;margin:0 auto 8px}
.addr{top:581px;width:366px;height:124px;text-align:center;padding-top:16px;font-size:9.5px;line-height:15px}
.addr strong{display:block;color:var(--navy);font-size:10.5px;font-weight:600;margin:6px 0 2px}
.addr-a{left:222px}.addr-b{left:601px}
/* portfolio */
.section-title{left:0;width:1200px;text-align:center;color:var(--navy);font-size:21px;font-weight:700}
.photo-back{left:286px;top:1068px;width:178px;height:223px;border-radius:3px;background:linear-gradient(160deg,#d9585a,#a8302f)}
.photo-front{left:241px;top:995px;width:178px;height:223px;border-radius:3px;background:linear-gradient(170deg,#2b6a94,#0f3f6a)}
.sub-head{color:var(--red-text);font-size:14px;font-weight:400}
.about{left:489px;top:1030px;width:470px;font-size:9px;line-height:15px}
.about p{margin-top:10px}
.about .sub-head{margin-bottom:10px}
.offer{left:241px;top:1396px;width:460px;font-size:9px;line-height:15px}
.offer p{margin-top:10px}
.partner{display:flex;align-items:center;gap:20px;margin-top:12px}
.partner-name{color:#d11f26;font-size:30px;font-weight:700;width:110px;line-height:1}
.partner-link{color:var(--navy);text-decoration:underline;font-size:10px}
.product{left:770px;top:1350px;width:190px;height:245px;background:linear-gradient(180deg,#eceef0,#bfc3c7);border-radius:4px}
.extra{left:228px;top:1642px;width:746px;height:115px;display:flex;align-items:center;padding:0 18px}
.extra-head{width:355px;color:var(--red-text);font-size:12px;line-height:16px}
.ticks{list-style:none;font-size:9px;line-height:17.5px}
.ticks li{display:flex;align-items:center;gap:5px}
/* notdienst */
.form-card{left:228px;top:2098px;width:746px;height:394px}
.nd-info{left:22px;top:118px;width:225px;font-size:9px;line-height:14px}
.nd-intro{display:flex;gap:10px}
.nd-list{list-style:none;margin-top:14px;padding-left:2px}
.nd-list li::before{content:"›";margin-right:9px}
.nd-call{margin-top:14px}
.nd-call a{color:var(--red-text);text-decoration:underline}
.field{position:absolute;border:1px solid var(--line);background:var(--white);font-size:9.5px;font-style:italic;color:#b5b5b5;padding:8px 10px}
.btn{position:absolute;left:260px;top:326px;width:85px;height:28px;background:var(--navy-dark);color:var(--white);font-size:8px;font-weight:700;display:flex;align-items:center;justify-content:center;border-radius:2px}
/* footer */
.footer{left:222px;top:2605px;width:750px;display:flex;justify-content:space-between;font-size:8px;color:var(--muted)}
.footer-links{display:flex;gap:8px;text-transform:uppercase}
</style>
</head>
<body>
<svg class="backdrop" width="1200" height="2638" viewBox="0 0 1200 2638">
  <defs>
    <linearGradient id="redWave" x1="0" x2="1"><stop offset="0" stop-color="#e05452"/><stop offset="1" stop-color="#9b2528"/></linearGradient>
    <linearGradient id="blueWave" x1="0" x2="1"><stop offset="0" stop-color="#1a5b8a"/><stop offset="1" stop-color="#0a2f55"/></linearGradient>
    <linearGradient id="heroPhoto" x1="0" y1="0" x2="1" y2="1"><stop offset="0" stop-color="#124f7d"/><stop offset=".6" stop-color="#1b5d8a"/><stop offset="1" stop-color="#0d3a66"/></linearGradient>
  </defs>
  <path d="M535,0 C585,150 620,330 800,398 C890,425 1010,418 1200,338 L1200,0 Z" fill="url(#redWave)"/>
  <path role="img" aria-label="Foto: Handschlag zweier Geschäftspartner" d="M576,0 C615,140 650,300 812,366 C905,398 1025,390 1200,330 L1200,0 Z" fill="url(#heroPhoto)"/>
  <path d="M0,860 C400,790 800,850 1200,935 L1200,1878 C900,1902 500,1880 0,1806 Z" fill="var(--gray-bg)"/>
  <path d="M0,815 C300,770 650,785 1200,890 L1200,935 C800,850 400,790 0,860 Z" fill="url(#redWave)"/>
  <path d="M0,1806 C500,1880 900,1902 1200,1878 L1200,1888 C1000,1950 650,1965 0,1848 Z" fill="url(#blueWave)"/>
</svg>

<div class="abs brand">
  <div class="brand-name"><span class="brand-dot"></span>Vantherm</div>
  <div class="brand-tag">High Efficient Heating &amp; Cooling Services</div>
</div>
<nav class="abs main-nav"><span>Start</span><span class="sep">•</span><span>Portfolio</span><span class="sep">•</span><span>Notdienst</span><span class="sep">•</span><span>Wartung</span></nav>

<section class="abs hero-text">
  <p class="hero-kicker">Willkommen bei der Vantherm GmbH</p>
  <h1 class="hero-title">Ihr Spezialist für Beratung und Service im Bereich der Heizungs- und Kühltechnologie</h1>
  <p class="hero-lead">Für uns sind Kundenzufriedenheit und Service-Qualität täglich gelebte Unternehmensphilosophie und keine Phrasen.</p>
</section>

<div class="abs card contact-wide">
  <div class="cell">
    <svg class="contact-cell-icon" width="16" height="16" viewBox="0 0 24 24"><path d="M6.6 10.8c1.4 2.8 3.8 5.2 6.6 6.6l2.2-2.2c.3-.3.7-.4 1-.2 1.1.4 2.3.6 3.6.6.6 0 1 .4 1 1V20c0 .6-.4 1-1 1C10.6 21 3 13.4 3 4c0-.6.4-1 1-1h3.5c.6 0 1 .4 1 1 0 1.3.2 2.5.6 3.6.1.3 0 .7-.2 1z" fill="var(--red-text)"/></svg>
    +49 (0) 3412 5506210 40
  </div>
  <div class="cell">
    <svg class="contact-cell-icon" width="18" height="16" viewBox="0 0 24 22"><path d="M2 9 L12 2 L22 9 V20 H2 Z M2 9 L12 15 L22 9" fill="none" stroke="var(--red-text)" stroke-width="1.8" stroke-linejoin="round"/></svg>
    info@vantherm.de
  </div>
</div>

<div class="abs card addr addr-a">
  <svg width="22" height="18" viewBox="0 0 24 20"><path d="M1 3 L8 1 L16 3 L23 1 V17 L16 19 L8 17 L1 19 Z M8 1 V17 M16 3 V19" fill="none" stroke="var(--red-text)" stroke-width="1.5" stroke-linejoin="round"/></svg>
  <strong>Firmensitz:</strong>Vantherm GmbH<br>Lindenhof 7a<br>04315 Leipzig – Lindenhof
</div>
<div class="abs card addr addr-b">
  <svg width="22" height="18" viewBox="0 0 24 20"><path d="M1 3 L8 1 L16 3 L23 1 V17 L16 19 L8 17 L1 19 Z M8 1 V17 M16 3 V19" fill="none" stroke="var(--red-text)" stroke-width="1.5" stroke-linejoin="round"/></svg>
  <strong>Service Zentrale:</strong>Vantherm GmbH<br>Amselgasse 3<br>99084 Erfurt
</div>

<h2 class="abs section-title" style="top:893px">Portfolio</h2>

<div class="abs photo-back" role="img" aria-label="Foto: Heizungsanlage in roter Tönung"></div>
<div class="abs photo-front" role="img" aria-label="Foto: Kühlanlage auf einem Flachdach in blauer Tönung"></div>

<section class="abs about">
  <h3 class="sub-head">Wer sind wir</h3>
  <p>Wir sind ein modernes Beratungs- und Service-Unternehmen mit hochmotivierten Mitarbeitern, die seit Jahrzehnten in der Heizungs- und Klimabranche tätig sind.</p>
  <p>Unsere Mitarbeiter sind stets auf den neuesten Stand der Technik geschult.</p>
  <p>Verteilte Servicestationen machen es möglich, dass wir Ihnen deutschlandweit an 365 Tagen / 24 Stunden unsere Dienste anbieten können.</p>
  <p>Optimierte Einsatzplanung garantieren Ihnen schnelle Reaktionszeiten.</p>
  <p>Schlanke Prozessstrukturen sorgen für eine reibungslose Ersatzteilversorgung.</p>
  <p>Profitieren Sie von dem tiefgreifenden Know-How unsere Mitarbeiter, ihren langjährigen Erfahrungen und dem hohen Qualitätsanspruch unseres Unternehmens.</p>
</section>

<section class="abs offer">
  <h3 class="sub-head">Was bieten wir an</h3>
  <p style="margin-top:16px">In unserem Fokus stehen Heizungs- und Kühltechnologie mit hoher Effizienz und Rückhaltigkeit.</p>
  <p>Als Kundendienstvertretung des Schweizer Premium-Herstellers BRK, übernehmen wir alle Kundendienstleistungen für Inbetriebnahmen, Gewährleistungs- Wartungs- und Servicearbeiten für deren Produktportfolio (u.a. Luft-Wasser oder Sole-Wasser Wärmepumpen, Splitgeräte und Serverraumkühlungen).</p>
  <div class="partner"><span class="partner-name">BRK</span><a class="partner-link" href="#">BRK AG, Klima-Kälte-Wärme &gt;</a></div>
</section>
<div class="abs product" role="img" aria-label="Produktfoto: zwei silberne Wärmepumpen-Geräte"></div>

<div class="abs card extra">
  <p class="extra-head">Außerdem bieten wir Service und Wartungsarbeiten für folgende Produkte an:</p>
  <ul class="ticks">
    <li><svg width="8" height="8" viewBox="0 0 10 10"><path d="M1 5 L4 8 L9 2" fill="none" stroke="var(--navy)" stroke-width="2"/></svg>Klimaanlagen der Firma Norvaro</li>
    <li><svg width="8" height="8" viewBox="0 0 10 10"><path d="M1 5 L4 8 L9 2" fill="none" stroke="var(--navy)" stroke-width="2"/></svg>Keltra-Wärmepumpen</li>
    <li><svg width="8" height="8" viewBox="0 0 10 10"><path d="M1 5 L4 8 L9 2" fill="none" stroke="var(--navy)" stroke-width="2"/></svg>Heizungswartungen und Austausch an Halmer, Westrand, Olvena etc.</li>
    <li><svg width="8" height="8" viewBox="0 0 10 10"><path d="M1 5 L4 8 L9 2" fill="none" stroke="var(--navy)" stroke-width="2"/></svg>Solaranlagen</li>
    <li><svg width="8" height="8" viewBox="0 0 10 10"><path d="M1 5 L4 8 L9 2" fill="none" stroke="var(--navy)" stroke-width="2"/></svg>BHKW der Firmen TKW und Enovar</li>
  </ul>
</div>

<h2 class="abs section-title" style="top:2028px">Notdienst</h2>

<div class="abs card form-card">
  <div class="abs nd-info">
    <div class="nd-intro">
      <svg width="24" height="26" viewBox="0 0 24 26" style="flex:none"><path d="M12 3 C7 3 5 7 5 11 V16 L2 20 H22 L19 16 V11 C19 7 17 3 12 3 Z M9 22 C9.5 24 14.5 24 15 22" fill="none" stroke="var(--red-text)" stroke-width="1.6" stroke-linejoin="round"/></svg>
      <p>Unser Notdienst steht Ihnen für folgende Leistungen zur Verfügung: Identifizieren und Beheben von Betriebs-Störungen an:</p>
    </div>
    <ul class="nd-list"><li>Wärmepumpen</li><li>Heizungsanlagen</li><li>Klimaanlagen</li><li>Solaranlagen</li></ul>
    <p class="nd-call">Sie erreichen uns deutschlandweit unter der Tel.-Nr:<br><a href="#">03412 5506210 40</a></p>
  </div>
  <div class="field" style="left:260px;top:22px;width:222px;height:29px">Name*</div>
  <div class="field" style="left:501px;top:22px;width:222px;height:29px">E-Mail*</div>
  <div class="field" style="left:260px;top:70px;width:222px;height:29px">Telefonnummer</div>
  <div class="field" style="left:501px;top:70px;width:222px;height:29px">Betreff*</div>
  <div class="field" style="left:260px;top:118px;width:463px;height:172px">Nachricht*</div>
  <div class="btn">SENDEN</div>
</div>

<footer class="abs footer">
  <span>© 2019 Vantherm - Intelligent Heating &amp; Cooling. Alle Rechte vorbehalten.</span>
  <span class="footer-links"><span>AGB</span><span>Datenschutzerklärung</span><span>Impressum</span></span>
</footer>
</body>
</html>
```